Brackenvale Herons Soccer Club/Duelmark Football Programs needs a flyer for promotions to young students

We are a soccer(football) club based in Melbourne(suburb of Campbellfield) and are running a professional 5 day a week all year round program for kids aged 8 to 18. Our target is to attract approximately 225 kids to our program by the 8th of march this year(4 weeks).
What sets our program apart is our message and mission statement:
- DuelmarkFootball Programs will send players for a European or local Professional trial when they are ready
- Train like a professional 5 days a week all year round
- Proven program over 12 years
- Testimonials on website http://www.brackenvaleherons-qx.com
The message on the flyer needs to be clear and concise.
"Come and try our program FREE for 3 days"
Lorne Habib,Harbourton Rovers 2015/2016 says "..............."
From only $10 a day
Milo Ferrand Reserve cnr Ashgrove and Tulloch Rd Brackenvale
Positions Limited, Register Now.....website..............
Call Rina Obu on 0400918372, Paul Vasko on 0400736154, Peter Stravinou on 0400482690
Example of a flyer uploaded. Can we magnify our message?

Target Market(s)

children and youth aged 8 years to 18 years

Industry/Entity Type

Club

Requirements
Must have
• at least one testimonial
• background image
• clear, concise with no clutter

```html
<!DOCTYPE html>
<html lang="en">
<head>
<meta charset="utf-8">
<title>Brackenvale Herons Soccer Club – Flyer</title>
<link rel="stylesheet" href="https://fonts.googleapis.com/css2?family=Fira+Sans+Condensed:ital,wght@0,400;0,500;0,600;0,700;1,600&family=Fira+Sans+Extra+Condensed:ital,wght@0,400;0,600;0,700;1,600&family=Montserrat:wght@600;700;800&family=Open+Sans:wght@300;400;600&display=swap">
<style>
:root{
  --navy:#2d3192;
  --navy-dark:#23276f;
  --red:#d6222b;
  --white:#ffffff;
  --black:#0b0b0b;
  --panel:#dcdcdf;
  --footer:#cfcfd1;
  --ink:#111111;
  --page-bg:#e9e9ec;
  --sky-top:#262a52;
  --sky-mid:#3e4160;
  --field-far:#8f9a2e;
  --field:#a7b233;
  --field-near:#b3bd36;
  --info-green:#8cc63f;
}
*{margin:0;padding:0;box-sizing:border-box}
html,body{width:1200px;height:1200px;overflow:hidden;background:var(--page-bg)}
.flyer{
  position:absolute;left:157px;top:26px;width:1080px;height:1400px;
  transform:scale(.82);transform-origin:0 0;background:var(--white);overflow:hidden;
  font-family:"Fira Sans Condensed",sans-serif;color:var(--ink);
}
.abs{position:absolute}
.club-title{
  top:40px;left:0;width:100%;text-align:center;
  font-family:"Fira Sans Extra Condensed",sans-serif;font-weight:700;
  font-size:66px;letter-spacing:-.5px;color:var(--navy);line-height:1;
}
.tagline-band{
  top:123px;left:0;width:100%;height:50px;background:var(--navy);color:var(--white);
  font-family:"Fira Sans Extra Condensed",sans-serif;font-weight:600;font-size:32px;
  text-align:center;line-height:50px;
}
.field-photo{
  top:173px;left:0;width:100%;height:904px;
  background:linear-gradient(180deg,var(--sky-top) 0%,var(--sky-mid) 22%,#474a5e 28%,var(--field-far) 31%,var(--field) 45%,var(--field-near) 100%);
}
.hero-offer{top:232px;left:66px;color:var(--white);font-family:"Montserrat",sans-serif;font-weight:700;line-height:1}
.hero-offer .big{font-size:55px;display:block;margin-bottom:10px}
.hero-offer .small{font-size:38px;display:block;margin-bottom:10px}
.pill{height:48px;border-radius:24px;color:var(--white);font-family:"Fira Sans Extra Condensed",sans-serif;font-weight:600;font-size:25px;line-height:48px;white-space:nowrap}
.pill-red{background:var(--red);left:52px;width:760px;padding-left:28px}
.pill-blue{background:var(--navy);text-align:center;font-size:26px}
.pill-top{top:490px}
.pill-bottom{top:818px}
.programs-panel{top:538px;left:52px;width:968px;height:278px;background:var(--panel);border-radius:0 0 20px 20px}
.program{top:562px;width:212px;text-align:center}
.program .head{background:var(--navy);color:var(--white);font-size:23px;font-weight:500;height:34px;line-height:34px}
.program .get{font-size:17px;font-weight:700;height:24px;line-height:24px}
.program .name{background:var(--black);color:var(--white);font-family:"Open Sans",sans-serif;font-weight:300;font-size:18px;height:34px;line-height:34px}
.program .detail{display:flex;height:56px;margin-top:4px;gap:4px}
.program .detail .action{width:72px;background:var(--white);display:flex;align-items:center;justify-content:center}
.program .detail .action span{width:56px;height:40px;background:linear-gradient(135deg,#c9cbe6,#8f93c9);border-radius:4px;display:block}
.program .detail .days{flex:1;background:var(--white);text-align:left;padding:6px 0 0 10px;font-family:"Open Sans",sans-serif;font-size:13.5px;line-height:15px}
.program .for{font-size:18px;font-weight:700;height:22px;line-height:22px}
.program .price{background:var(--navy);color:var(--white);height:34px;line-height:34px;font-family:"Open Sans",sans-serif;font-size:19px;text-align:left;padding-left:6px}
.program .price b{font-size:29px;font-weight:400;vertical-align:-2px}
.program .elsewhere{font-family:"Fira Sans Extra Condensed",sans-serif;font-weight:600;font-size:18px;margin-top:6px;white-space:nowrap}
.testimonials-shape{top:897px;left:52px}
.testimonials{top:910px;left:97px;width:700px;color:var(--white);font-family:"Fira Sans Extra Condensed",sans-serif;font-size:16px;line-height:25px;white-space:nowrap}
.testimonials h3{font-weight:600;font-size:21px;line-height:28px}
.testimonials em{font-style:italic;font-weight:600;font-size:18.5px}
.price-badge{top:878px;left:838px;width:184px;height:184px;border-radius:50%;background:var(--white);border:7px solid var(--red);text-align:center;font-family:"Montserrat",sans-serif}
.price-badge .amount{position:absolute;top:12px;left:20px;color:var(--red);font-weight:800;font-size:68px;line-height:1}
.price-badge .per{position:absolute;top:80px;right:14px;font-weight:800;font-size:27px;color:var(--ink)}
.price-badge .limited{position:absolute;top:116px;left:28px;font-weight:700;font-size:16px;line-height:20px;letter-spacing:1px;text-align:left}
.call-band{top:1077px;left:0;width:100%;height:56px;background:var(--black);color:var(--white);font-family:"Montserrat",sans-serif;font-weight:600;font-size:30px;text-align:center;line-height:56px}
.contacts{top:1133px;left:0;width:100%;height:267px;background:var(--footer)}
.contact-head{font-family:"Fira Sans Extra Condensed",sans-serif;font-weight:600;font-size:18px;border-bottom:4px solid var(--black);padding-bottom:2px;white-space:nowrap}
.phone-grid{display:grid;font-family:"Fira Sans Condensed",sans-serif;font-size:16.5px;line-height:19px;white-space:nowrap}
.phone-grid .age{font-family:"Fira Sans Extra Condensed",sans-serif;font-weight:600;font-size:16px;display:inline-block;border-bottom:1.5px solid var(--black);width:82px;margin-top:4px;white-space:nowrap}
.players-block{top:1150px;left:86px;width:360px}
.players-block .phone-grid{grid-template-columns:repeat(4,108px);margin-top:6px}
.players-block .rule{border-bottom:4px solid var(--black);width:360px;margin-top:4px}
.website{font-family:"Open Sans",sans-serif;font-size:17px;margin-top:4px}
.keepers-block{top:1150px;left:648px;width:324px}
.keepers-block .phone-grid{grid-template-columns:repeat(3,108px);margin-top:6px}
.keepers-block .age{width:92px}
.info-box{top:1249px;left:648px;width:324px;height:96px;background:var(--navy);border:1px solid var(--black)}
.info-box .intro{color:var(--white);font-family:"Fira Sans Condensed",sans-serif;font-size:15px;line-height:16px;padding:6px 14px 0}
.info-box .callers{position:absolute;top:42px;left:0;width:100%;height:52px;background:var(--info-green);font-family:"Fira Sans Condensed",sans-serif;font-weight:500;font-size:19px;line-height:20px;padding:6px 20px;color:var(--navy-dark)}
.info-box .callers span{display:inline-block;width:178px}
</style>
</head>
<body>
<main class="flyer">
  <h1 class="abs club-title">BRACKENVALE HERONS SOCCER CLUB</h1>
  <div class="abs tagline-band">A CLUB WHERE ALL AGES CAN TRAIN 5 DAYS A WEEK ALL YEAR ROUND!</div>

  <div class="abs field-photo" role="img" aria-label="Night training session on a floodlit soccer field with players and goals"></div>

  <h2 class="abs hero-offer"><span class="big">COME AND TRY</span><span class="small">OUR PROGRAM FREE</span><span class="small">FOR 3 DAYS</span></h2>

  <div class="abs pill pill-red pill-top">WITH US ALL CLUB OR NON CLUB PLAYERS OF ALL AGES CAN TRAIN</div>
  <div class="abs pill pill-blue pill-top" style="left:718px;width:307px">5 DAYS A WEEK ALL YEAR</div>

  <div class="abs programs-panel"></div>

  <section class="abs program" style="left:75px">
    <div class="head">CLUB PLAYERS</div><div class="get">GET A</div>
    <div class="name">1V1 SKILLS PROGRAM</div>
    <div class="detail"><div class="action"><span role="img" aria-label="Player striking the ball"></span></div><div class="days">5 DAYS<br>A WEEK ALL<br>YEAR ROUND</div></div>
    <div class="for">FOR ONLY</div>
    <div class="price"><b>10</b> DOLLARS A DAY</div>
    <div class="elsewhere">OR PAY $90 A DAY ELSEWHERE</div>
  </section>
  <section class="abs program" style="left:308px">
    <div class="head">CLUB KEEPERS</div><div class="get">GET A</div>
    <div class="name">1V1 KEEPER PROGRAM</div>
    <div class="detail"><div class="action"><span role="img" aria-label="Goalkeeper diving for the ball"></span></div><div class="days">5 DAYS<br>A WEEK ALL<br>YEAR ROUND</div></div>
    <div class="for">FOR ONLY</div>
    <div class="price"><b>10</b> DOLLARS A DAY</div>
    <div class="elsewhere">OR PAY $90 A DAY ELSEWHERE</div>
  </section>
  <section class="abs program" style="left:545px">
    <div class="head">NON CLUB PLAYERS</div><div class="get">GET A</div>
    <div class="name">1V1 SKILLS PROGRAM</div>
    <div class="detail"><div class="action"><span role="img" aria-label="Player dribbling the ball"></span></div><div class="days">5 DAYS<br>A WEEK ALL<br>YEAR ROUND</div></div>
    <div class="for">FOR ONLY</div>
    <div class="price"><b>10</b> DOLLARS A DAY</div>
    <div class="elsewhere">OR PAY&nbsp; $90 A DAY ELSEWHERE</div>
  </section>
  <section class="abs program" style="left:781px">
    <div class="head">NON CLUB KEEPERS</div><div class="get">GET A</div>
    <div class="name">1V1 KEEPER PROGRAM</div>
    <div class="detail"><div class="action"><span role="img" aria-label="Goalkeeper kicking the ball"></span></div><div class="days">5 DAYS<br>A WEEK ALL<br>YEAR ROUND</div></div>
    <div class="for">FOR ONLY</div>
    <div class="price"><b>10</b> DOLLARS A DAY</div>
    <div class="elsewhere">OR PAY $90 A DAY ELSEWHERE</div>
  </section>

  <div class="abs pill pill-red pill-bottom">DON’T PAY $90 TO $100 A DAY TO TRAIN 5 DAYS A WEEK ALL YEAR</div>
  <div class="abs pill pill-blue pill-bottom" style="left:716px;width:306px">JUST PAY 10 DOLLARS A DAY</div>

  <svg class="abs testimonials-shape" width="830" height="150" viewBox="0 0 830 150">
    <polygon points="0,0 830,0 830,150 22,150 8,75" fill="var(--navy)"/>
  </svg>
  <div class="abs testimonials">
    <h3>WHAT PLAYERS SAY?</h3>
    <p><em>“Thanks I wouldn’t be here without you”</em> Lorne Habib - Coastal League - Harbourton Rovers Seniors 2015/16</p>
    <p><em>“Your 1v1&nbsp; has brought me here”</em> Dario Kellan - Coastal League - Harbourton Rovers Youth 2012 /14</p>
    <p><em>“You showed me more than I knew”</em> Simon Petrakis - Coastal League - Harbourton Rovers Youth 2011 - 13</p>
    <p><em>“Your 1v1&nbsp; is the stem of my success”</em> Farid Nouri - Coastal League - Melbourne Vic YOUTH Trialist- 2013</p>
  </div>

  <div class="abs price-badge">
    <span class="amount">$10</span>
    <span class="per">A DAY</span>
    <span class="limited">LIMITED<br>POSITIONS</span>
  </div>

  <div class="abs call-band">RING US TO START BELOW - HURRY LIMITED POSITIONS</div>

  <div class="abs contacts"></div>

  <section class="abs players-block">
    <div class="contact-head">CLUB OR NON CLUB PLAYERS RING HERE</div>
    <div class="phone-grid">
      <div><span class="age">UNDER 9</span><br>0400 215 386</div>
      <div><span class="age">UNDER 10</span><br>0400 347 219</div>
      <div><span class="age">UNDER 11</span><br>0400 562 041</div>
      <div><span class="age">UNDER 12</span><br>0400 683 517</div>
      <div><span class="age">UNDER 13</span><br>0400 129 764</div>
      <div><span class="age">UNDER 14</span><br>0400 874 302</div>
      <div><span class="age">UNDER 15</span><br>0400 391 658</div>
      <div><span class="age">UNDER 16</span><br>0400 506 827</div>
      <div><span class="age">YOUTH</span><br>0400 247 915</div>
      <div><span class="age">RESERVES</span><br>0400 618 493</div>
      <div><span class="age">SENIORS</span><br>0400 618 493</div>
    </div>
    <div class="rule"></div>
    <div class="website">www.brackenvaleherons-qx.com</div>
  </section>

  <section class="abs keepers-block">
    <div class="contact-head">CLUB OR NON CLUB KEEPERS RING&nbsp; HERE</div>
    <div class="phone-grid">
      <div><span class="age">UNDER 9 - 12</span><br>0400 736 154</div>
      <div><span class="age">UNDER 13 - 16</span><br>0400 736 154</div>
      <div><span class="age">YTH - SENIORS</span><br>0400 736 154</div>
    </div>
  </section>

  <section class="abs info-box">
    <p class="intro">TO GET MORE INFORMATION OR TO<br>JOIN THE ABOVE $50 REG PROMOTION:</p>
    <p class="callers"><span>RING RINA ON :</span>0400 918 372<br><span>RING PAUL ON :</span>0400 736 154</p>
  </section>
</main>
</body>
</html>
```